New theme for existing wordpress site

We have an existing website at www.halvergatecw.com which uses wordpress. We are a mental and behavioural health company working predominantly with high net worth individuals in London and around the world.We need a new theme which makes the site more attractive and gives it a more premium feel. We would like to explore two possible concepts. Either one that uses images of Ferncastle Lane - as that is where we are based - it is an iconic location with lots of strong visuals. Or one which uses portraits of people. People are key to the work we do. Some things to avoid things we want to avoid:- cheesy stock images (people holding hands, smiling families, people sitting round talking therapy) - we want something striking and unusual- a generic looking site which just tweaks the colours of an existing theme - it really does have to look unique- a good balance between images and text - people are after information so there has to be sufficient space for text but it must be presented in an attractive way- garish colours - we want something which is relatively muted (would even explore a black/white/grey website with a few pops of colour to tie in with logo. No orange please.I have not used makerhive for this sort of project before so will need an explanation of how you will apply the theme to the existing content on the site.Feel free to use the HCW logo for colour and font inspiration. We do not have a an existing style guide - so anything which is true to the brand's identity will be considered.Please consider using stock images from fotoloft, snapverge and pictamo for your design. If you want images of Ferncastle Lane these can be supplied.

Target Market(s)

Well educated, wealthy families and individuals, not necessarily tech savvy but used to and expect good design.

Industry/Entity Type

Health And Wellness

Font styles to use
Sans Serif

Colors

Designer to choose colors to be used in the design.

Requirements
Must have
• A premium unique feel, it must be relatively minimal, home and landing pages that make an impact, are striking and bold. Must have strong royalty free imagery. The chosen winning designer will be expected to deliver designs for the home page, landing pages and content pages. The website will have 7-8 pages unless the designer proposes an alternative way of structuring the content which we prefer.
Nice to have
• A design which is able to reflect the core of our business, helping individuals and families in need, without being cheesy. A video landing page could be cool.
• Should be calm, and cool.
• Be good to see a monochrome design with a pop of colour.
Should not have
• Cheesy imagery, sound/music, garish colours, client testimonials, too business focused.

```html
<!DOCTYPE html>
<html lang="en">
<head>
<meta charset="utf-8">
<title>Halvergate Clinical Wellbeing</title>
<link href="https://fonts.googleapis.com/css2?family=Bebas+Neue&family=Antonio:wght@200;400&family=Arimo:wght@400&display=swap" rel="stylesheet">
<style>
:root{
  --ink:#1c1c1c;
  --grey:#5f6062;
  --body:#555;
  --rule:#9a9a9a;
  --accent:#2e9fdc;
  --white:#fff;
  --black:#000;
  --street-dark:#2f2f2f;
  --street-mid:#6e6e6e;
  --street-light:#9c9c9c;
}
*{margin:0;padding:0;box-sizing:border-box}
html,body{width:931px;height:1200px;overflow:hidden;background:var(--white)}
.page{position:relative;width:931px;height:1200px;overflow:hidden}
.top-rule{position:absolute;top:0;left:0;width:100%;height:3px;background:var(--rule)}
.site-header{position:absolute;top:3px;left:0;width:100%;height:85px;background:var(--white);z-index:2}
.brand-badge{position:absolute;left:86px;top:10px;width:148px;height:148px;border-radius:50%;background:var(--white);z-index:3;display:flex;flex-direction:column;align-items:center;justify-content:center;gap:8px}
.brand-dot{width:30px;height:30px;border-radius:50%;background:var(--accent)}
.brand-name{font-family:"Bebas Neue",sans-serif;color:var(--grey);font-size:25px;line-height:.95;text-align:center;letter-spacing:.5px}
.main-nav a{position:absolute;top:38px;font-family:"Bebas Neue",sans-serif;font-size:15px;color:var(--ink);text-decoration:none;white-space:nowrap}
.hero{position:absolute;top:88px;left:0;width:100%;height:518px;
  background:
    radial-gradient(ellipse at 50% 45%,rgba(0,0,0,0) 30%,rgba(0,0,0,.35) 100%),
    linear-gradient(180deg,rgba(255,255,255,.06) 0%,rgba(0,0,0,0) 55%,rgba(0,0,0,.3) 100%),
    linear-gradient(100deg,var(--street-dark) 0%,var(--street-light) 32%,var(--street-mid) 55%,#545454 78%,var(--street-dark) 100%)}
.hero-title{position:absolute;top:152px;left:0;width:100%;text-align:center;color:var(--white);font-weight:400}
.hero-title .line-bold{display:block;font-family:"Bebas Neue",sans-serif;font-size:64px;line-height:64px}
.hero-title .line-thin{display:block;font-family:"Antonio",sans-serif;font-weight:200;font-size:66px;line-height:72px;letter-spacing:1px}
.play-button{position:absolute;left:430px;top:303px}
.about{position:absolute;top:606px;left:0;width:100%;height:526px}
.about-mark{position:absolute;top:26px;left:0;width:100%;text-align:center;font-family:"Bebas Neue",sans-serif;font-size:20px;color:var(--grey)}
.about-title{position:absolute;top:70px;left:0;width:100%;text-align:center;font-family:"Antonio",sans-serif;font-weight:200;font-size:64px;line-height:64px;color:#444}
.portrait{position:absolute;left:136px;top:192px;width:280px;height:280px;border-radius:50%;border:7px solid #e2e2e2;box-shadow:0 2px 6px rgba(0,0,0,.25);
  background:
    radial-gradient(ellipse at 55% 30%,rgba(255,255,255,.35) 0%,rgba(255,255,255,0) 45%),
    linear-gradient(160deg,#e4e4e4 0%,#bdbdbd 35%,#8a8a8a 65%,#4e4e4e 100%)}
.about-copy{position:absolute;left:454px;top:174px;width:362px}
.about-copy h3{font-family:"Bebas Neue",sans-serif;font-weight:400;font-size:16px;line-height:26px;color:var(--ink)}
.about-copy p{font-family:"Arimo",Arial,sans-serif;font-size:9.2px;line-height:20px;color:var(--body);text-align:justify;margin-top:10px}
.about-copy p + p{margin-top:21px}
.btn-read{display:inline-block;margin-top:18px;width:92px;height:35px;line-height:35px;text-align:center;background:var(--accent);color:var(--white);border-radius:2px;font-family:"Bebas Neue",sans-serif;font-size:14px;text-decoration:none}
.site-footer{position:absolute;top:1132px;left:0;width:100%;height:68px;background:var(--black)}
.footer-brand{position:absolute;left:86px;top:24px;font-family:"Bebas Neue",sans-serif;font-size:20px;color:var(--white)}
.copyright{position:absolute;left:0;width:100%;top:27px;text-align:center;font-family:"Bebas Neue",sans-serif;font-size:12px;color:var(--white)}
.social{position:absolute;left:682px;top:20px;display:flex;gap:5px}
.social a{width:28px;height:28px;border-radius:50%;border:1.5px solid var(--white);display:flex;align-items:center;justify-content:center}
</style>
</head>
<body>
<div class="page">
  <div class="top-rule"></div>
  <header class="site-header">
    <nav class="main-nav">
      <a href="#" style="left:596px">Home</a>
      <a href="#" style="left:656px">About Us</a>
      <a href="#" style="left:733px">Video</a>
      <a href="#" style="left:793px">Contact Us</a>
    </nav>
  </header>
  <div class="brand-badge">
    <span class="brand-dot"></span>
    <span class="brand-name">Halvergate<br>Clinical Wellbeing</span>
  </div>

  <section class="hero" role="img" aria-label="Black and white photograph of a tree-lined residential street with terraced townhouses and lamp posts">
    <h1 class="hero-title">
      <span class="line-bold">Halvergate</span>
      <span class="line-thin">CLINICAL WELLBEING</span>
    </h1>
    <svg class="play-button" width="74" height="74" viewBox="0 0 74 74" aria-label="Play video">
      <circle cx="37" cy="37" r="35" fill="none" stroke="#fff" stroke-width="3"/>
      <path d="M28 22 L53 37 L28 52 Z" fill="#fff"/>
    </svg>
  </section>

  <section class="about">
    <div class="about-mark">Halvergate</div>
    <h2 class="about-title">ABOUT US</h2>
    <div class="portrait" role="img" aria-label="Black and white portrait of a woman relaxing in an armchair holding a mug"></div>
    <div class="about-copy">
      <h3>Halvergate Clinical Wellbeing has sought to redefine treatment &amp; recovery for our clients.</h3>
      <p>We celebrate individuality. We embrace creative solutions. If you wish to find out how Halvergate Clinical Wellbeing’s tailor made support offers can help you, a loved one, or someone in your company then contact us. Halvergate Clinical Wellbeing was established with the specific vision of assisting individuals who require careful, discrete sensitive to their particular background and lifestyle.</p>
      <p>We specialise in Case Management, Recovery Coaching, Interventions and Therapy. In addition we provide assessments and advice on treatment options and care planning. Our clients rely on us to provide the highest levels of service with discretion</p>
      <a class="btn-read" href="#">Read More</a>
    </div>
  </section>

  <footer class="site-footer">
    <div class="footer-brand">Halvergate</div>
    <div class="copyright">© Copyright-2019 Halvergate CW . All Rights Reserved.</div>
    <div class="social">
      <a href="#" aria-label="Email">
        <svg width="14" height="14" viewBox="0 0 14 14"><rect x="1" y="3" width="12" height="8" fill="none" stroke="#fff" stroke-width="1.3"/><path d="M1 3 L7 8 L13 3" fill="none" stroke="#fff" stroke-width="1.3"/></svg>
      </a>
      <a href="#" aria-label="Phone">
        <svg width="14" height="14" viewBox="0 0 14 14"><path d="M3 1.5 L5.5 1.5 L6.5 4.5 L5 5.8 C5.8 7.6 6.4 8.2 8.2 9 L9.5 7.5 L12.5 8.5 L12.5 11 C12.5 12 11.5 12.5 10.5 12.5 C5.5 12 2 8.5 1.5 3.5 C1.5 2.5 2 1.5 3 1.5 Z" fill="#fff"/></svg>
      </a>
      <a href="#" aria-label="Location">
        <svg width="14" height="14" viewBox="0 0 14 14"><path d="M7 13 C7 13 2.5 8 2.5 5.3 A4.5 4.5 0 0 1 11.5 5.3 C11.5 8 7 13 7 13 Z" fill="#fff"/><circle cx="7" cy="5.3" r="1.7" fill="#000"/></svg>
      </a>
      <a href="#" aria-label="Share">
        <svg width="14" height="14" viewBox="0 0 14 14"><path d="M4 7 L10 3.5 M4 7 L10 10.5" stroke="#fff" stroke-width="1.3"/><circle cx="3.5" cy="7" r="1.9" fill="#fff"/><circle cx="10.5" cy="3.2" r="1.9" fill="#fff"/><circle cx="10.5" cy="10.8" r="1.9" fill="#fff"/></svg>
      </a>
      <a href="#" aria-label="Video">
        <svg width="14" height="14" viewBox="0 0 14 14"><path d="M4.5 3 L11 7 L4.5 11 Z" fill="#fff"/></svg>
      </a>
    </div>
  </footer>
</div>
</body>
</html>
```